Local fast-growing company in the service sector

We are looking for a modern business card design, which should also appear on our letterheads

Target Market(s)

Private and industrial sectors

Contact Information for Business Card

Vorname Name
Lindkofer Str. 18
71468 Ostwaldingen
Tel.: 07163-418259-0
Name@kovaltec-pbz.de

Colors
9d9d9d
919191
aaaaaa

Requirements
Must have
• The logo (file) in silver

```html
<!DOCTYPE html>
<html lang="de">
<head>
<meta charset="utf-8">
<title>Kovaltec – Visitenkarten-Entwürfe</title>
<link rel="stylesheet" href="https://fonts.googleapis.com/css2?family=Questrial&family=Montserrat:wght@700&family=Cormorant+Garamond:ital,wght@1,500&family=Libre+Caslon+Text:wght@400&display=swap">
<style>
  :root {
    --paper: #ffffff;
    --frame: #6f6f6f;
    --ink: #262626;
    --card-dark: #1d1d1b;
    --silver: #aaaaaa;
    --silver-mid: #9d9d9d;
    --silver-deep: #919191;
    --text-light: #c9c9c9;
    --green: #1f8a3b;
    --divider: #1a1a1a;
  }
  * { box-sizing: border-box; margin: 0; padding: 0; }
  html, body { width: 1200px; height: 663px; overflow: hidden; background: var(--paper); }
  .sheet { position: relative; width: 1200px; height: 663px; background: var(--paper); }

  .panel { position: absolute; top: 0; height: 662px; border: 1px solid var(--frame); }
  .panel--left { left: 0; width: 588px; }
  .panel--right { left: 612px; width: 588px; }

  .variant-number {
    position: absolute; font-family: "Questrial", sans-serif; font-size: 50px;
    color: var(--ink); line-height: 1;
  }

  .card { position: absolute; width: 462px; height: 257px; overflow: hidden; }
  .card--light {
    left: 70px; top: 52px; border: 1px solid var(--ink); border-radius: 14px;
    background: linear-gradient(135deg, #f4f4f4 0%, #ffffff 35%, #e9e9e9 60%, #fafafa 100%);
  }
  .card--dark-floral { left: 70px; top: 358px; border-radius: 14px; background: var(--card-dark); }
  .card--dark-paisley { left: 687px; top: 54px; border-radius: 14px; background: var(--card-dark); }
  .card--green-band { left: 687px; top: 366px; border: 1px solid var(--frame); background: var(--paper); }

  .brand { position: absolute; display: flex; align-items: center; gap: 10px; }
  .brand__mark { width: 14px; height: 14px; background: var(--silver); }
  .brand__name {
    font-family: "Questrial", sans-serif; color: var(--silver-mid); letter-spacing: 1px;
  }
  .card--light .brand { left: 0; right: 0; top: 72px; justify-content: center; }
  .card--light .brand__name { font-size: 46px; color: var(--silver-deep); }
  .card--light .brand__mark { width: 22px; height: 22px; background: var(--silver-deep); }
  .card--dark-floral .brand { left: 34px; top: 60px; }
  .card--dark-floral .brand__name { font-size: 38px; color: var(--silver); }
  .card--dark-floral .brand__mark { width: 18px; height: 18px; }
  .card--dark-paisley .brand { left: 17px; top: 30px; }
  .card--dark-paisley .brand__name { font-family: "Cormorant Garamond", serif; font-style: italic; font-weight: 500; font-size: 34px; color: var(--silver); }

  .rule { position: absolute; left: 14px; width: 434px; top: 184px; height: 2px; background: var(--divider); }

  .contact { position: absolute; font-family: "Questrial", sans-serif; font-size: 11.5px; line-height: 15.5px; }
  .contact strong { font-family: "Montserrat", sans-serif; font-weight: 700; font-size: 11px; }
  .card--light .contact { color: var(--ink); top: 194px; }
  .contact--address { left: 14px; }
  .contact--phone { left: 263px; }
  .card--dark-floral .contact { left: 17px; top: 160px; color: var(--text-light); line-height: 15.2px; }
  .card--dark-floral .contact strong { color: #ffffff; }
  .card--dark-paisley .contact {
    left: 14px; top: 158px; color: var(--text-light);
    font-family: "Cormorant Garamond", serif; font-style: italic; font-weight: 500;
    font-size: 13.5px; line-height: 14.8px;
  }
  .card--green-band .contact {
    left: 0; right: 0; top: 114px; text-align: center; color: var(--ink);
    font-family: "Libre Caslon Text", serif; font-size: 14px; line-height: 18.5px;
  }

  .ornament { position: absolute; }
  .ornament--corner {
    right: 0; top: 0; width: 125px; height: 257px;
    background: radial-gradient(ellipse at 100% 0%, #8a8a8a 0%, #4a4a48 40%, rgba(29,29,27,0) 75%),
                radial-gradient(ellipse at 100% 100%, #5f5f5d 0%, rgba(29,29,27,0) 55%);
  }
  .ornament--paisley {
    left: 207px; top: 16px; width: 250px; height: 218px; border-radius: 50% 45% 50% 40%;
    background: radial-gradient(ellipse at 45% 60%, #8e8e8c 0%, #5a5a58 45%, rgba(29,29,27,0) 75%);
  }

  .band { position: absolute; left: 0; top: 0; width: 100%; height: 66px; background: var(--green); }
  .band__edge { position: absolute; left: 0; top: 66px; width: 100%; height: 3px; background: var(--silver); }
  .band .brand { left: 0; right: 0; top: 16px; justify-content: center; }
  .band .brand__name { font-family: "Libre Caslon Text", serif; font-size: 28px; color: #d6d6d6; }
  .band .brand__mark { background: #d6d6d6; }
  .ornament--scroll {
    top: 18px; width: 95px; height: 32px; border-radius: 16px;
    background: linear-gradient(90deg, rgba(220,232,222,0.2), #cfdccf 50%, rgba(220,232,222,0.2));
  }
  .ornament--scroll-left { left: 23px; }
  .ornament--scroll-right { left: 344px; }
</style>
</head>
<body>
<main class="sheet">
  <section class="panel panel--left">
    <span class="variant-number" style="left:26px; top:262px;">1</span>
    <span class="variant-number" style="left:26px; top:540px;">2</span>
  </section>
  <section class="panel panel--right">
    <span class="variant-number" style="left:24px; top:208px;">3</span>
    <span class="variant-number" style="left:24px; top:480px;">4</span>
  </section>

  <article class="card card--light">
    <div class="brand"><span class="brand__mark"></span><span class="brand__name">Kovaltec</span></div>
    <div class="rule"></div>
    <p class="contact contact--address">Kovaltec Hausdienste GmbH &amp; Co. KG<br>Lindkoferstraße 18<br>71468 Ostwaldingen</p>
    <p class="contact contact--phone">Telefon: <strong>+49 (7163) 4182590</strong><br>Telefax: <strong>+49 (7163) 4182599</strong><br>info@kovaltec-pbz.de</p>
  </article>

  <article class="card card--dark-floral">
    <div class="ornament ornament--corner" role="img" aria-label="Silbernes florales Eckornament"></div>
    <div class="brand"><span class="brand__mark"></span><span class="brand__name">Kovaltec</span></div>
    <p class="contact">Kovaltec Hausdienste GmbH &amp; Co. KG<br>Lindkoferstraße 18<br>71468 Ostwaldingen<br>Telefon: <strong>+49 (7163) 4182590</strong><br>Telefax: <strong>+49 (7163) 4182599</strong><br>info@kovaltec-pbz.de</p>
  </article>

  <article class="card card--dark-paisley">
    <div class="ornament ornament--paisley" role="img" aria-label="Großes silbernes Paisley-Ornament"></div>
    <div class="brand"><span class="brand__mark"></span><span class="brand__name">Kovaltec</span></div>
    <p class="contact">Kovaltec Hausdienste GmbH &amp; Co. KG<br>Lindkoferstraße 18<br>71468 Ostwaldingen<br>Telefon: +49 (7163) 4182590<br>Telefax: +49 (7163) 4182599<br>info@kovaltec-pbz.de</p>
  </article>

  <article class="card card--green-band">
    <div class="band">
      <div class="ornament ornament--scroll ornament--scroll-left" role="img" aria-label="Helles Rankenornament links"></div>
      <div class="brand"><span class="brand__mark"></span><span class="brand__name">Kovaltec</span></div>
      <div class="ornament ornament--scroll ornament--scroll-right" role="img" aria-label="Helles Rankenornament rechts"></div>
    </div>
    <div class="band__edge"></div>
    <p class="contact">Kovaltec Hausdienste GmbH &amp; Co. KG<br>Lindkoferstraße 18<br>71468 Ostwaldingen<br>Telefon: +49 (7163) 4182590<br>Telefax: +49 (7163) 4182599<br>info@kovaltec-pbz.de</p>
  </article>
</main>
</body>
</html>
```